Coloring Book Cover for Adults

I'd like a unique book cover design for a coloring book we are making for adults. The book cover is for an 8.5"x11" book. I need both the front and back cover created. We will want to include some text about the book on the back cover so there should be room for that. It will be less than 100 words.

1) The title is:

Take a Damn Breath and Shade: Grown-Up Coloring Book for Quiet Evenings

2) A swear word may appear on the cover, however it should similar to some of the examples included.

3) I'd prefer the background be in black or white so that the picture and color "pop" off the page more.

I've included 4 example covers that I really like. Something similar to these is preferred.

Target Market(s)

Adults age 25-65

Industry/Entity Type

Publishing Company

Font styles to use
Decorative
Script

Requirements
Must have
• Colorful cover with black or white background.
Should not have
• No Slurs, or homophobic language -

```html
<!DOCTYPE html>
<html lang="en">
<head>
<meta charset="utf-8">
<title>Take a Damn Breath and Shade</title>
<link rel="stylesheet" href="https://fonts.googleapis.com/css2?family=Black+Ops+One&family=Permanent+Marker&family=Gochi+Hand&display=swap">
<style>
  :root {
    --ink: #0d0d0d;
    --paper: #ffffff;
    --magenta: #e8168c;
    --orange: #f7842a;
    --yellow: #f6ee5a;
    --green: #7cc242;
    --mint: #a7dcc0;
    --teal: #5cc8d8;
    --purple: #9a3f96;
  }
  * { box-sizing: border-box; margin: 0; padding: 0; }
  html, body { width: 933px; height: 1200px; overflow: hidden; background: var(--paper); }
  .cover { position: relative; width: 933px; height: 1200px; overflow: hidden; }
  .cover-pattern {
    position: absolute; inset: 0;
    background: linear-gradient(160deg,
      var(--yellow) 0%, var(--orange) 14%, var(--magenta) 28%, var(--purple) 40%,
      var(--teal) 52%, var(--green) 62%, var(--mint) 72%, var(--magenta) 84%, var(--orange) 100%);
  }
  .title-panel {
    position: absolute; left: 133px; top: 96px; width: 671px; height: 1010px;
    background: var(--paper); border: 7px solid var(--ink);
    display: flex; flex-direction: column; align-items: center;
  }
  .title-lead, .title-tail {
    font-family: "Permanent Marker", cursive;
    color: var(--ink); font-size: 104px; line-height: 1;
  }
  .title-lead { margin-top: 120px; }
  .title-big { display: block; margin-top: 14px; }
  .title-tail { margin-top: 16px; }
  .subtitle {
    font-family: "Gochi Hand", cursive;
    color: var(--ink); font-size: 31px; margin-top: 96px; white-space: nowrap;
  }
</style>
</head>
<body>
<main class="cover">
  <div class="cover-pattern" role="img" aria-label="Colourful hand-drawn zentangle pattern of swirls, waves and zigzag bands in pink, orange, yellow, green, teal and purple"></div>
  <section class="title-panel">
    <h1 class="title-lead">Take a</h1>
    <svg class="title-big" width="600" height="300" viewBox="0 0 600 300" role="img" aria-label="Damn Breath">
      <defs>
        <linearGradient id="letter-fill" x1="0" y1="0" x2="1" y2="1">
          <stop offset="0" stop-color="#e8168c"/>
          <stop offset="0.2" stop-color="#9a3f96"/>
          <stop offset="0.38" stop-color="#f6ee5a"/>
          <stop offset="0.55" stop-color="#5cc8d8"/>
          <stop offset="0.72" stop-color="#f7842a"/>
          <stop offset="0.88" stop-color="#7cc242"/>
          <stop offset="1" stop-color="#e8168c"/>
        </linearGradient>
      </defs>
      <g font-family="Black Ops One, sans-serif" fill="url(#letter-fill)" stroke="#0d0d0d" stroke-width="10" stroke-linejoin="round" paint-order="stroke" text-anchor="middle">
        <text x="300" y="132" font-size="150" textLength="430" lengthAdjust="spacingAndGlyphs">DAMN</text>
        <text x="300" y="282" font-size="150" textLength="580" lengthAdjust="spacingAndGlyphs">BREATH</text>
      </g>
    </svg>
    <p class="title-tail">and Shade</p>
    <p class="subtitle">Grown-Up Coloring Book for Quiet Evenings</p>
  </section>
</main>
</body>
</html>
```